Business cards - ZELTO Roofing & Siding

We need simple business cards made up for our Roofing & Siding business based in Calgary Alberta.
The logo on one side of the card and potentially our slogan "Built with trust, verified by time".
The other side could have:
-A small logo
-Rep name:
-Rep cell phone:
-Rep email:
-Office phone: 403-688-2904
-Website: PrairieTopCrafters.com

We would like to incorporate the colours from our logo, especially the lite blue on the jpeg file. I have attached the ai file and jpeg file. We like the colours better on the jpeg file.

```html
<!DOCTYPE html>
<html lang="en">
<head>
<meta charset="utf-8">
<title>ZELTO Roofing &amp; Siding – Business Cards</title>
<link href="https://fonts.googleapis.com/css2?family=Montserrat:wght@400;500;600;700&display=swap" rel="stylesheet">
<style>
  :root {
    --backdrop: #3b3b3b;
    --card-black: #1b1b1c;
    --card-white: #ffffff;
    --sky-blue: #1a8cf0;
    --deep-blue: #0f6cc4;
    --ink: #111111;
    --light-text: #f4f4f4;
  }
  * { margin: 0; padding: 0; box-sizing: border-box; }
  html, body {
    width: 1200px; height: 1200px; overflow: hidden;
    background: var(--backdrop);
    font-family: "Montserrat", sans-serif;
  }
  .sheet {
    position: relative; width: 1200px; height: 1200px;
  }
  .card {
    position: absolute; left: 220px;
    width: 760px; height: 434px;
    border-radius: 26px; overflow: hidden;
    box-shadow: 0 18px 40px rgba(0,0,0,0.45);
  }
  .card--front { top: 120px; background: var(--card-black); }
  .card--back { top: 646px; background: var(--card-black); }

  .front-split { position: absolute; inset: 0; }

  .brand {
    position: absolute;
    font-weight: 700;
    letter-spacing: 2px;
    display: flex; align-items: center; gap: 14px;
  }
  .brand__mark { width: 22px; height: 22px; background: var(--sky-blue); }
  .brand__name { display: flex; flex-direction: column; line-height: 1; }
  .brand__word { font-size: 64px; letter-spacing: 6px; }
  .brand__tag { font-size: 19px; letter-spacing: 5px; margin-top: 10px; }

  .brand--front { left: 200px; top: 70px; color: var(--ink); }
  .brand--back {
    left: 50%; top: 50%; transform: translate(-50%, -50%);
    color: var(--card-white);
  }
  .brand--back .brand__word { font-size: 96px; letter-spacing: 10px; }
  .brand--back .brand__tag { font-size: 28px; letter-spacing: 7px; margin-top: 14px; }
  .brand--back .brand__mark { width: 30px; height: 30px; }

  .rep {
    position: absolute; left: 80px; top: 318px;
    border-left: 6px solid var(--sky-blue);
    padding-left: 14px;
  }
  .rep__name {
    color: var(--sky-blue); font-weight: 700; font-size: 38px; line-height: 1;
  }
  .rep__title {
    color: var(--light-text); font-weight: 500; font-size: 17px;
    margin-top: 6px; letter-spacing: 0.5px;
  }

  .contacts {
    position: absolute; left: 448px; top: 268px;
    list-style: none;
  }
  .contacts__item {
    display: flex; align-items: center; gap: 12px;
    color: var(--light-text); font-size: 17px; font-weight: 400;
    height: 30px;
  }
  .contacts__icon { width: 20px; height: 20px; flex: none; }
</style>
</head>
<body>
<main class="sheet">

  <section class="card card--front" aria-label="Card front with contact details">
    <svg class="front-split" viewBox="0 0 760 434" preserveAspectRatio="none" aria-hidden="true">
      <polygon points="0,0 760,0 760,150 0,318" fill="var(--card-white)"/>
      <polygon points="0,318 760,150 760,158 0,326" fill="var(--sky-blue)"/>
    </svg>

    <div class="brand brand--front">
      <span class="brand__mark"></span>
      <span class="brand__name">
        <span class="brand__word">ZELTO</span>
        <span class="brand__tag">ROOFING &amp; SIDING</span>
      </span>
    </div>

    <div class="rep">
      <p class="rep__name">JOHN DOE</p>
      <p class="rep__title">CEO | FOUNDER</p>
    </div>

    <ul class="contacts">
      <li class="contacts__item">
        <svg class="contacts__icon" viewBox="0 0 20 20" aria-hidden="true">
          <rect x="5" y="1.5" width="10" height="17" rx="2" fill="none" stroke="var(--sky-blue)" stroke-width="1.8"/>
          <circle cx="10" cy="15.5" r="1" fill="var(--sky-blue)"/>
        </svg>
        403-688-2904
      </li>
      <li class="contacts__item">
        <svg class="contacts__icon" viewBox="0 0 20 20" aria-hidden="true">
          <path d="M4 2 L7.5 2 L9 6.5 L7 8 C8 10.5 9.5 12 12 13 L13.5 11 L18 12.5 L18 16 C18 17 17 18 16 18 C8.5 17.5 2.5 11.5 2 4 C2 3 3 2 4 2 Z" fill="var(--sky-blue)"/>
        </svg>
        403-688-2904
      </li>
      <li class="contacts__item">
        <svg class="contacts__icon" viewBox="0 0 20 20" aria-hidden="true">
          <rect x="1.5" y="4" width="17" height="12" fill="none" stroke="var(--sky-blue)" stroke-width="1.8"/>
          <path d="M1.5 4 L10 11 L18.5 4" fill="none" stroke="var(--sky-blue)" stroke-width="1.8"/>
        </svg>
        email@youremail.com
      </li>
      <li class="contacts__item">
        <svg class="contacts__icon" viewBox="0 0 20 20" aria-hidden="true">
          <circle cx="10" cy="10" r="8.2" fill="none" stroke="var(--sky-blue)" stroke-width="1.6"/>
          <ellipse cx="10" cy="10" rx="3.6" ry="8.2" fill="none" stroke="var(--sky-blue)" stroke-width="1.4"/>
          <line x1="1.8" y1="10" x2="18.2" y2="10" stroke="var(--sky-blue)" stroke-width="1.4"/>
          <line x1="3.5" y1="5.5" x2="16.5" y2="5.5" stroke="var(--sky-blue)" stroke-width="1.2"/>
          <line x1="3.5" y1="14.5" x2="16.5" y2="14.5" stroke="var(--sky-blue)" stroke-width="1.2"/>
        </svg>
        prairietopcrafters.com
      </li>
    </ul>
  </section>

  <section class="card card--back" aria-label="Card back with company name">
    <div class="brand brand--back">
      <span class="brand__mark"></span>
      <span class="brand__name">
        <span class="brand__word">ZELTO</span>
        <span class="brand__tag">ROOFING &amp; SIDING</span>
      </span>
    </div>
  </section>

</main>
</body>
</html>
```